Expo show design Banner , banners in the size of 640x100 and 1456x180

For a **main-hall banner**, the message needs to work from a distance: one dominant statement, a short product line, and a strong reason to visit the booth. Since your main lightbox is approximately **79" × 94"**, I would avoid trying to explain everything.

### Recommended banner copy

**VARNOLD GLOBAL | PFP AUTHORITY**

# NORTH AMERICA’S
# PFP FABRIC SOURCE

### ONE OF THE LARGEST IN-STOCK SELECTIONS
### READY FOR DYE SUBLIMATION

**PFP FABRICS • DYE-SUB PAPER • TOWELS & BLANKETS**
**PROTECTION TISSUE • PRINTING SUPPLIES**

### IN STOCK. READY TO PRINT. READY TO SHIP.

**VISIT US — BOOTH #_____**

I especially like **“IN STOCK. READY TO PRINT. READY TO SHIP.”** because it communicates the advantage Varnold has over overseas mills and competitors very quickly.

If you are comfortable substantiating the “largest” claim, I would make it even stronger:

# THE LARGEST SELECTION OF
# IN-STOCK PFP FABRICS
# IN NORTH AMERICA

**PFP FABRICS | DYE-SUB PAPER | TOWELS & BLANKETS | PROTECTION TISSUE**

### YOUR ONE-STOP DYE-SUBLIMATION SOURCE

**BOOTH #_____**

For the design, I would make **“IN-STOCK PFP FABRICS”** the biggest words on the entire banner—not the Varnold name. Someone walking through the hall should understand what you sell in **2–3 seconds**. Keep all critical copy well inside the safe zone; the supplied template specifically requires logos/text/contact information to stay within it.

I would also use a **dark/black technical background + white typography + Varnold red highlights**, with subtle imagery/textures of white performance fabric and dye-sub paper. Since this is a backlit SEG display, the artwork guide recommends a formulated “True Black” rather than K-only black, which can appear gray when illuminated.

**My preferred headline combination is:**

> **THE LARGEST SELECTION OF**
> **IN-STOCK PFP FABRICS**
> **IN NORTH AMERICA**
>
> **READY FOR DYE SUBLIMATION**
>
> *In Stock. Ready to Print. Ready to Ship.*

That is much stronger for a hall banner than listing too many technical details.

Viist site for more ideas and info www.Varnold.example

```html
<!DOCTYPE html>
<html lang="en">
<head>
<meta charset="utf-8">
<title>Varnold Global — In-Stock PFP Fabrics Banner</title>
<link rel="stylesheet" href="https://fonts.googleapis.com/css2?family=Archivo:ital,wght@0,600;0,700;0,800;0,900;1,800&display=swap">
<style>
  :root {
    --page: #ffffff;
    --true-black: #0c0c0d;
    --ink: #141414;
    --white: #ffffff;
    --red: #dc2330;
    --red-deep: #9e1520;
  }
  html, body {
    margin: 0;
    padding: 0;
    width: 1029px;
    height: 1200px;
    overflow: hidden;
    background: var(--page);
  }
  .banner {
    display: block;
    width: 1029px;
    height: 1200px;
    font-family: "Archivo", "Helvetica Neue", Arial, sans-serif;
  }
  .panel { fill: var(--true-black); }
  .accent-red { fill: var(--red); }
  .accent-deep { fill: var(--red-deep); }
  .brand-name { fill: var(--white); font-weight: 800; font-size: 76px; }
  .program-label { fill: var(--white); font-weight: 800; font-style: italic; font-size: 24px; }
  .program-badge { fill: none; stroke: var(--white); stroke-width: 3; }
  .brand-tagline { fill: var(--white); font-weight: 700; font-size: 24px; letter-spacing: 2px; }
  .intro-line { fill: var(--white); font-weight: 800; font-size: 62px; letter-spacing: 4px; }
  .hero-white { fill: var(--white); font-weight: 900; font-size: 156px; }
  .hero-red { fill: var(--red); font-weight: 900; font-size: 112px; }
  .region-line { font-weight: 800; font-size: 74px; letter-spacing: 5px; }
  .region-white { fill: var(--white); }
  .region-red { fill: var(--red); }
  .ribbon { fill: var(--white); stroke: var(--red); stroke-width: 6; stroke-linejoin: round; }
  .ribbon-text { fill: var(--ink); font-weight: 800; font-size: 42px; }
  .truck { fill: var(--red); }
  .product-frame { fill: none; stroke: var(--red); stroke-width: 4; }
  .product-icon { fill: none; stroke: var(--white); stroke-width: 3.5; stroke-linejoin: round; stroke-linecap: round; }
  .product-label { fill: var(--white); font-weight: 700; font-size: 27px; letter-spacing: 0.5px; }
  .source-line { fill: var(--white); font-weight: 700; font-size: 29px; letter-spacing: 2.6px; }
  .booth-bar { fill: var(--red); }
  .booth-arrow { fill: var(--true-black); }
  .booth-text { fill: var(--white); font-weight: 800; font-size: 31px; letter-spacing: 2px; }
</style>
</head>
<body>
<svg class="banner" viewBox="0 0 1792 2100" preserveAspectRatio="xMidYMid meet" xmlns="http://www.w3.org/2000/svg">
  <defs>
    <linearGradient id="product-photo-tones" x1="0" y1="0" x2="1" y2="0.15">
      <stop offset="0" stop-color="#f1f1f1"/>
      <stop offset="0.4" stop-color="#e4e4e4"/>
      <stop offset="0.58" stop-color="#d2d2d2"/>
      <stop offset="0.72" stop-color="#e5562a"/>
      <stop offset="0.85" stop-color="#f2b533"/>
      <stop offset="1" stop-color="#2b5fb3"/>
    </linearGradient>
    <clipPath id="panel-clip"><rect x="163" y="173" width="1450" height="1725"/></clipPath>
  </defs>

  <rect class="panel" x="163" y="173" width="1450" height="1725"/>

  <g clip-path="url(#panel-clip)">
    <polygon class="accent-red" points="163,173 330,173 163,322"/>
    <polygon class="accent-deep" points="345,173 420,173 163,405 163,338"/>

    <g role="img" aria-label="Photo of folded white towels, a roll of dye-sub paper and a brightly printed sublimated fabric on a grey surface">
      <polygon class="accent-red" points="930,1240 1613,820 1613,870 975,1250"/>
      <polygon fill="url(#product-photo-tones)" points="163,1228 975,1238 1613,880 1613,1762 880,1652 163,1735"/>
    </g>
    <polygon class="accent-red" points="163,1665 400,1722 163,1762"/>

    <polygon class="accent-red" points="1613,648 1613,690 1300,1010 1262,1010"/>

    <polygon class="ribbon" points="1613,418 1613,584 1268,996 1246,1000 1134,838 1138,818"/>
  </g>

  <text class="brand-name" x="1040" y="304" textLength="262" lengthAdjust="spacingAndGlyphs">Varnold</text>
  <text class="program-label" x="1392" y="262" textLength="152" lengthAdjust="spacingAndGlyphs">STOCK PROGRAM</text>
  <circle class="program-badge" cx="1340" cy="304" r="24"/>
  <circle class="program-badge" cx="1402" cy="304" r="24"/>
  <circle class="program-badge" cx="1463" cy="304" r="24"/>
  <circle class="program-badge" cx="1525" cy="304" r="24"/>
  <text class="brand-tagline" x="1036" y="367" textLength="512" lengthAdjust="spacingAndGlyphs">VARNOLD GLOBAL | PFP AUTHORITY</text>

  <text class="intro-line" x="228" y="437" textLength="404" lengthAdjust="spacingAndGlyphs">THE LARGEST</text>
  <text class="intro-line" x="228" y="500" textLength="430" lengthAdjust="spacingAndGlyphs">SELECTION OF</text>
  <text class="hero-white" x="226" y="684" textLength="820" lengthAdjust="spacingAndGlyphs">IN-STOCK</text>
  <text class="hero-red" x="226" y="797" textLength="822" lengthAdjust="spacingAndGlyphs">PFP FABRICS</text>
  <text class="region-line" x="226" y="890" textLength="730" lengthAdjust="spacingAndGlyphs"><tspan class="region-white">IN NORTH </tspan><tspan class="region-red">AMERICA</tspan></text>

  <g transform="translate(1245 790) rotate(-43)">
    <text class="ribbon-text" x="0" y="0" textLength="205" lengthAdjust="spacingAndGlyphs">IN STOCK</text>
    <text class="ribbon-text" x="2" y="46" textLength="345" lengthAdjust="spacingAndGlyphs">READY TO PRINT</text>
    <text class="ribbon-text" x="5" y="93" textLength="312" lengthAdjust="spacingAndGlyphs">READY TO SHIP</text>
  </g>
  <g class="truck" transform="translate(1242 870) rotate(-37.5)">
    <rect x="-28" y="-22" width="42" height="32" rx="3"/>
    <path d="M16 -12 h14 l10 12 v10 h-24 z"/>
    <circle cx="-16" cy="14" r="6"/>
    <circle cx="26" cy="14" r="6"/>
    <rect x="-50" y="-16" width="16" height="4"/>
    <rect x="-54" y="-6" width="20" height="4"/>
    <rect x="-48" y="4" width="14" height="4"/>
  </g>

  <g class="product">
    <rect class="product-frame" x="229" y="974" width="104" height="105" rx="14"/>
    <g class="product-icon">
      <ellipse cx="262" cy="1020" rx="12" ry="18"/>
      <path d="M262 1002 h28 a12 18 0 0 1 0 36 h-28"/>
      <path d="M290 1038 l28 -10 l-56 22"/>
    </g>
    <text class="product-label" x="228" y="1135">PFP</text>
    <text class="product-label" x="228" y="1167">FABRICS</text>
  </g>
  <g class="product">
    <rect class="product-frame" x="414" y="974" width="105" height="105" rx="14"/>
    <g class="product-icon">
      <ellipse cx="447" cy="1022" rx="12" ry="18"/>
      <path d="M447 1004 h38 a12 18 0 0 1 0 36 h-38"/>
      <path d="M485 1040 l18 -8"/>
    </g>
    <text class="product-label" x="413" y="1135">DYE-SUB</text>
    <text class="product-label" x="413" y="1167">PAPER</text>
  </g>
  <g class="product">
    <rect class="product-frame" x="600" y="974" width="105" height="105" rx="14"/>
    <g class="product-icon">
      <rect x="620" y="1036" width="68" height="16" rx="8"/>
      <rect x="622" y="1020" width="64" height="16" rx="8"/>
      <rect x="626" y="1004" width="56" height="16" rx="8"/>
    </g>
    <text class="product-label" x="599" y="1128">TOWELS &amp;</text>
    <text class="product-label" x="599" y="1160">BLANKETS</text>
  </g>
  <g class="product">
    <rect class="product-frame" x="786" y="974" width="105" height="105" rx="14"/>
    <g class="product-icon">
      <path d="M802 1026 l36 -22 l36 22 l-36 22 z"/>
      <path d="M802 1034 l36 22 l36 -22"/>
      <path d="M802 1042 l36 22 l36 -22"/>
    </g>
    <text class="product-label" x="785" y="1135">PROTECTION</text>
    <text class="product-label" x="785" y="1167">TISSUE</text>
  </g>
  <g class="product">
    <rect class="product-frame" x="989" y="974" width="105" height="105" rx="14"/>
    <g class="product-icon">
      <rect x="1034" y="996" width="14" height="10" rx="2"/>
      <path d="M1028 1006 h26 l4 8 v42 h-34 v-42 z"/>
      <rect x="1032" y="1024" width="18" height="24"/>
    </g>
    <text class="product-label" x="988" y="1135">PRINTING</text>
    <text class="product-label" x="988" y="1167">SUPPLIES</text>
  </g>

  <text class="source-line" x="250" y="1815" textLength="708" lengthAdjust="spacingAndGlyphs">YOUR ONE-STOP DYE-SUBLIMATION SOURCE</text>
  <polygon class="booth-bar" points="990,1771 1550,1771 1550,1834 1022,1834 1004,1802"/>
  <polygon class="booth-arrow" points="995,1786 1040,1786 1040,1770 1080,1802 1040,1834 1040,1818 1010,1818"/>
  <text class="booth-text" x="1092" y="1815" textLength="344" lengthAdjust="spacingAndGlyphs">VISIT US — BOOTH #</text>
</svg>
</body>
</html>
```